Business card for plumber

I need a business card for my plumbing company.
on it should:
Surname
position
E-mail
Telephone & mobile phone
Website
Please everything as placeholders / fantasy names.
We stand for high quality, hygiene and professionalism.

Colours:
# 606060 anthracite
# f7931e orange
# 2b89cc blue

Industry/Entity Type

Plumber

Contact Information for Business Card

folgt...

```html
<!DOCTYPE html>
<html lang="en">
<head>
<meta charset="utf-8">
<title>Kessler Haustechnik – Business Card</title>
<link href="https://fonts.googleapis.com/css2?family=Source+Sans+3:wght@400;600;700&display=swap" rel="stylesheet">
<style>
  :root {
    --anthracite: #5c5c5c;
    --orange: #f7931e;
    --blue: #2b89cc;
    --paper: #f4f4f4;
    --stage: #e4e4e4;
    --ink: #555555;
    --rule: #8a8a8a;
    --white: #ffffff;
  }
  * { margin: 0; padding: 0; box-sizing: border-box; }
  html, body {
    width: 1200px; height: 960px; overflow: hidden;
    background: var(--stage);
    font-family: "Source Sans 3", "Myriad Pro", Arial, sans-serif;
  }
  .canvas { position: relative; width: 1200px; height: 960px; }
  .card { position: absolute; left: 340px; width: 520px; height: 336px; overflow: hidden; }

  /* Front */
  .card--front { top: 128px; background: var(--anthracite); }
  .front-mark {
    position: absolute; left: -70px; top: 150px;
    width: 210px; height: 210px; border-radius: 50%;
    background: var(--orange);
  }
  .wordmark { position: absolute; color: var(--blue); font-weight: 700; line-height: 1; text-transform: uppercase; }
  .card--front .wordmark { right: 30px; top: 143px; text-align: right; }
  .wordmark__name { display: block; font-size: 36px; letter-spacing: 0.5px; }
  .wordmark__tag { display: block; font-size: 17px; letter-spacing: 4.2px; margin-top: 1px; }
  .services { position: absolute; right: 31px; top: 244px; list-style: none; text-align: right; }
  .services li {
    color: var(--white); font-size: 14px; font-weight: 600;
    line-height: 22px; text-transform: uppercase;
  }
  .services li::after { content: "•"; color: var(--orange); margin-left: 5px; }

  /* Back */
  .card--back { top: 503px; background: var(--paper); }
  .card--back .brand { position: absolute; right: 31px; top: 72px; display: flex; align-items: center; gap: 10px; }
  .brand__dot { width: 34px; height: 34px; border-radius: 50%; background: var(--orange); }
  .card--back .wordmark { position: static; }
  .card--back .wordmark__name { font-size: 30px; }
  .card--back .wordmark__tag { font-size: 14px; letter-spacing: 3.5px; }
  .person { position: absolute; left: 33px; top: 175px; }
  .person__name { color: var(--blue); font-size: 18px; font-weight: 700; line-height: 1.2; }
  .person__role { color: var(--ink); font-size: 14px; line-height: 1.3; }
  .divider { position: absolute; left: 33px; top: 224px; width: 456px; height: 2px; background: var(--rule); }
  .contacts { position: absolute; left: 33px; top: 237px; list-style: none; }
  .contacts li { display: flex; align-items: center; gap: 6px; color: var(--ink); font-size: 14px; line-height: 18.5px; }
  .contacts svg { width: 12px; height: 12px; fill: var(--orange); flex: none; }
  .footer-bands { position: absolute; left: 0; bottom: 0; width: 520px; height: 34px; }
  .website {
    position: absolute; right: 31px; bottom: 9px;
    color: var(--white); font-size: 14px;
  }
</style>
</head>
<body>
<main class="canvas">
  <section class="card card--front" aria-label="Card front">
    <div class="front-mark"></div>
    <div class="wordmark">
      <span class="wordmark__name">Kessler</span>
      <span class="wordmark__tag">Haustechnik</span>
    </div>
    <ul class="services">
      <li>Plumbing</li>
      <li>Heating 24h Emergency Service</li>
      <li>Maintenance</li>
    </ul>
  </section>

  <section class="card card--back" aria-label="Card back">
    <div class="brand">
      <div class="brand__dot"></div>
      <div class="wordmark">
        <span class="wordmark__name">Kessler</span>
        <span class="wordmark__tag">Haustechnik</span>
      </div>
    </div>
    <div class="person">
      <p class="person__name">Daniel Hartmann</p>
      <p class="person__role">President</p>
    </div>
    <div class="divider"></div>
    <ul class="contacts">
      <li><svg viewBox="0 0 12 12"><path d="M2.4 0.6 4.3 2.9 3.3 4.2c.7 1.6 2 2.9 3.6 3.6l1.3-1 2.3 1.9-1.2 1.9C5.2 10.6 1 6.6.6 1.7Z"/></svg>555-014-2290</li>
      <li><svg viewBox="0 0 12 12"><path d="M3 0h6a1 1 0 0 1 1 1v10a1 1 0 0 1-1 1H3a1 1 0 0 1-1-1V1a1 1 0 0 1 1-1Zm.5 1.5v8h5v-8Zm2.5 8.7a.6.6 0 1 0 0 1.2.6.6 0 0 0 0-1.2Z"/></svg>555-014-2290</li>
      <li><svg viewBox="0 0 12 12"><path d="M0 2h12v8H0Zm1 1v.4l5 3.3 5-3.3V3Zm0 1.6V9h10V4.6L6 7.9Z"/></svg>daniel@kesslerhaustechnik.com</li>
    </ul>
    <svg class="footer-bands" viewBox="0 0 520 34" aria-hidden="true">
      <rect x="0" y="16" width="245" height="18" fill="#2b89cc"/>
      <path d="M225 34 L253 10 Q261 3 272 3 L520 3 L520 34 Z" fill="#f7931e"/>
    </svg>
    <span class="website">www.kesslerhaustechnik.com</span>
  </section>
</main>
</body>
</html>
```